Plate Parade! Digital Order Web App

This is a web app on mobile phone, for consumers to order food inside a restaurant using their phones. we have done up the flow but we need to revamp UI design. pls have a look at our current web on your mobile phone:
https://demo.pesanly.app/o/KWLM/274615

CURRENT DESIGN.
1. food category on left side, always shown. menu items in list view with image.
2. when we click on an item, there is popup page, to select modifiers, or quantity.
3. order review page(cart page) is quite messy now, need a complete new look.
4 payment page(no need to design, handle by Paxtel)
5. order confirmation page. success or error return

DESIGN requirements:
please browse through and click to order with current page above. we have put in lots of thoughts and effort for current flow, the new design should base on this flow.
1. web app. no zoom in/out is allowed for users. responsive html to suit different mobile phone screen size. modern fonts.
2. PAGES needed:
home/welcome page,
well laid out menu items page,
single item page, with add on choice and modifier
cart page(to include recommended items, ordered item list, remove item total, changeable quantity,
confirmation page(success, fail)

DELIVERABLES - responsive html, fonts, images asset such as icons, animation, button images(suitable for commercial use without further third party loyalty fee)

Hi all if we have left a comment on ur design, please revise accordingly and we will conclude it soon!

Target Market(s)

young diners who order food on their mobile phone.

Industry/Entity Type

Restaurant

Coding

Coded - Design and coding required

Number of Pages Required

5+ page

Colors

Designer to choose colors to be used in the design.

Requirements
Must have
• - lively, appetising colors while making the page easy to read. easy on eyes.
• - consistency. fonts used.
Nice to have
• - 2 color schemes
• - html codes. we will top up if you can deliver coded html.
Should not have
• - should not have more than 3 colors
• - should not have more than 3 different fonts
• - should not use colors that are dull

```html
<!DOCTYPE html>
<html lang="en">
<head>
<meta charset="utf-8">
<meta name="viewport" content="width=676, user-scalable=no">
<title>Plate Parade! – Vegetable Menu</title>
<link rel="stylesheet" href="https://fonts.googleapis.com/css2?family=Source+Sans+3:wght@400;600;700&family=Noto+Sans+SC:wght@400&display=swap">
<style>
  :root {
    --navy: #2b2f6e;
    --navy-soft: #3a3f80;
    --orange: #f15a24;
    --page: #e8e8eb;
    --card: #ffffff;
    --ink: #111111;
    --muted: #7a7a7a;
    --tab-dim: rgba(255,255,255,0.55);
  }
  * { box-sizing: border-box; margin: 0; padding: 0; }
  html, body { width: 676px; height: 1200px; overflow: hidden; }
  body {
    position: relative;
    background: var(--page);
    font-family: "Source Sans 3", "Helvetica Neue", Arial, sans-serif;
    color: var(--ink);
  }
  .app-header {
    position: absolute; left: 0; top: 0; width: 676px; height: 266px;
    overflow: hidden;
  }
  .header-backdrop {
    position: absolute; inset: 0;
    background: linear-gradient(100deg, #272b66 0%, #343979 45%, #3d427f 70%, #2f336f 100%);
  }
  .menu-toggle { position: absolute; left: 33px; top: 78px; }
  .restaurant-name {
    position: absolute; left: 0; right: 0; top: 70px;
    text-align: center; color: #fff; font-size: 37px; font-weight: 400; letter-spacing: 0.3px;
  }
  .search-button { position: absolute; left: 603px; top: 66px; }
  .category-tabs {
    position: absolute; left: 0; top: 154px; width: 676px; height: 60px;
    white-space: nowrap; font-size: 29px;
  }
  .category-tab { position: absolute; top: 0; color: var(--tab-dim); }
  .category-tab.is-active { color: #fff; }
  .category-tab.is-active::after {
    content: ""; position: absolute; left: 25px; width: 88px; top: 52px;
    height: 3px; background: #fff;
  }
  .order-summary {
    position: absolute; left: 180px; top: 228px; width: 312px; height: 74px;
    background: #fff; border-radius: 37px;
    box-shadow: 0 6px 14px rgba(0,0,0,0.12);
    display: flex; align-items: center; justify-content: center;
    color: var(--navy); font-size: 22px; letter-spacing: 0.2px;
  }
  .order-summary .order-total { font-size: 28px; margin-left: 6px; }
  .cart-button {
    position: absolute; left: 541px; top: 213px; width: 101px; height: 101px;
    border-radius: 50%; background: var(--orange);
    box-shadow: 0 5px 10px rgba(0,0,0,0.22);
    display: flex; align-items: center; justify-content: center;
  }
  .dish-card {
    position: absolute; left: 12px; width: 651px; height: 195px;
    background: var(--card); border-radius: 3px;
    box-shadow: 0 1px 3px rgba(0,0,0,0.08);
  }
  .dish-photo {
    position: absolute; left: 23px; top: 30px; width: 134px; height: 134px; border-radius: 6px;
  }
  .dish-name { position: absolute; left: 176px; top: 24px; font-size: 30px; font-weight: 400; }
  .dish-name-zh {
    position: absolute; left: 176px; top: 66px; font-size: 22px; color: var(--muted);
    font-family: "Noto Sans SC", "Source Sans 3", sans-serif;
  }
  .dish-price { position: absolute; left: 176px; top: 108px; font-size: 31px; font-weight: 700; }
  .add-button {
    position: absolute; left: 511px; top: 124px; width: 115px; height: 39px;
    background: var(--orange); border-radius: 6px; color: #fff;
    font-size: 25px; font-weight: 700; letter-spacing: 0.5px;
    display: flex; align-items: center; justify-content: center; gap: 10px;
    box-shadow: 0 2px 3px rgba(0,0,0,0.15);
  }
</style>
</head>
<body>
  <header class="app-header">
    <div class="header-backdrop" role="img" aria-label="Dimmed photo of a table with chopsticks and a teacup in navy tint"></div>
    <svg class="menu-toggle" width="44" height="33" viewBox="0 0 44 33" aria-label="Menu">
      <g stroke="#fff" stroke-width="2.4" stroke-linecap="round">
        <line x1="2" y1="2" x2="42" y2="2"/>
        <line x1="2" y1="16.5" x2="36" y2="16.5"/>
        <line x1="2" y1="31" x2="30" y2="31"/>
      </g>
    </svg>
    <h1 class="restaurant-name">Name of Restaurant</h1>
    <svg class="search-button" width="52" height="50" viewBox="0 0 52 50" aria-label="Search">
      <circle cx="20" cy="20" r="17" fill="none" stroke="#fff" stroke-width="3"/>
      <line x1="32.5" y1="32.5" x2="48" y2="47" stroke="#fff" stroke-width="3.4" stroke-linecap="round"/>
    </svg>
    <nav class="category-tabs">
      <span class="category-tab" style="left:23px">Main</span>
      <span class="category-tab" style="left:139px">Drinks</span>
      <span class="category-tab is-active" style="left:269px">Vegetable</span>
      <span class="category-tab" style="left:452px">Lunches</span>
      <span class="category-tab" style="left:617px">Desserts</span>
    </nav>
  </header>

  <div class="order-summary">YOUR ORDER: <span class="order-total">S$70</span></div>
  <div class="cart-button" aria-label="Cart">
    <svg width="58" height="50" viewBox="0 0 58 50">
      <g fill="none" stroke="#fff" stroke-width="3.2" stroke-linejoin="round" stroke-linecap="round">
        <path d="M3 5 H11 L18 33 H47 L53 12 H14"/>
      </g>
      <circle cx="22" cy="42" r="3.6" fill="#fff"/>
      <circle cx="43" cy="42" r="3.6" fill="#fff"/>
    </svg>
  </div>

  <main class="dish-list">
    <article class="dish-card" style="top:339px">
      <div class="dish-photo" role="img" aria-label="Photo of grilled romaine lettuce" style="background:linear-gradient(150deg,#9bb860,#6f9640 55%,#b7cf86)"></div>
      <h2 class="dish-name">Grilled Romaine Lettuce</h2>
      <p class="dish-name-zh">烤油麦菜</p>
      <p class="dish-price">S$1.30</p>
      <div class="add-button">ADD <span>+</span></div>
    </article>
    <article class="dish-card" style="top:546px">
      <div class="dish-photo" role="img" aria-label="Photo of grilled oyster mushroom skewers" style="background:linear-gradient(150deg,#7a4a22,#b27a35 50%,#5a3418)"></div>
      <h2 class="dish-name">Grilled Oyster Mushroom</h2>
      <p class="dish-name-zh">烤耗菇</p>
      <p class="dish-price">S$1.30</p>
      <div class="add-button">ADD <span>+</span></div>
    </article>
    <article class="dish-card" style="top:753px">
      <div class="dish-photo" role="img" aria-label="Photo of grilled shitake mushroom skewers" style="background:linear-gradient(150deg,#b0441d,#4d2b19 45%,#2c1a10)"></div>
      <h2 class="dish-name">Grilled Shitake Mushroom</h2>
      <p class="dish-name-zh">烤香菇</p>
      <p class="dish-price">S$1.30</p>
      <div class="add-button">ADD <span>+</span></div>
    </article>
    <article class="dish-card" style="top:961px">
      <div class="dish-photo" role="img" aria-label="Photo of grilled string bean skewers" style="background:linear-gradient(150deg,#5b3a22,#6fa63c 35%,#4f8a2c)"></div>
      <h2 class="dish-name">Grilled String Bean</h2>
      <p class="dish-name-zh">烤四季豆</p>
      <p class="dish-price">S$1.30</p>
      <div class="add-button">ADD <span>+</span></div>
    </article>
    <article class="dish-card" style="top:1168px">
      <div class="dish-photo" role="img" aria-label="Photo of a grilled vegetable skewer" style="background:linear-gradient(150deg,#7a4a22,#4d2b19)"></div>
      <h2 class="dish-name">Grilled Shitake Mushroom</h2>
    </article>
  </main>
</body>
</html>
```